Systems and Technology Consultants - Website

Design & Build a website for a new company which operates in the Systems and Technology space for Transportation, Government and Commercial sectors.

Overall design should be minimalist in nature.
Should also have a feed that provides news and event updates on the main page.
Logo has already been awarded and should be incorporated into the site.

We like the overall layout, functionality and simplicity of the below sites. Submitted designs could be similar to or a combination of the aspects on these sites, or perhaps a whole different concept - we are open to new ideas.
Vortrane.com
Merp.it

Update 1 Dated 27 May 2014

All I am moving away from the Merp.it website and would like it to be more aligned with Vortrane.com not only in layout but in functionality. I will be extending the deadline of this design brief for two weeks to incorporate additional requirements and will add addtional funding to the project.

Apologies for not having more information available to provide but with so many submissions its getting confusing.

Thanks Dermot
Updates

Please note that the brief has been updated and the deadline has been extended.

Important: We will need two language versions of the website, English and Arabic; the website is hosted on HostPeak

Hello All, Thank you for your submissions. We have narrowed it down to the final 6 designers and I just wanted to take a moment and provide a bit of feedback regarding the concepts that we like and the modifications we are looking for. First, let me mention some of the design functions we like. - At the top of the homepage we really like the "region" or "language" tab so that the website can be viewed in both English and Arabic. - We like the homepage to have clear color variation so that the different sections of the homepage are distinct. Additionally, we like the bottom portion of the homepage to be in red. We feel that draws attention to our contact information. Again, we would like the colors to integrate black, gray-scale, red, etc. - Having a search tab at the top of the home page, or integrated into the main image, so that the site is easy to navigate. - We especially like the main image to have the scrolling tabs at the bottom so it is easy to browse the services offered (Consultancy, Solutions Architecture, Masters Systems Integration, Independent Design Review). - In regards to the services offered tab we really like the idea that a few people presented that have the outside of our logo with an icon in the middle of consultancy, solutions, etc., etc. Secondly, as mentioned in our brief we really enjoy the design of vortrane site. Specially, we enjoy the strong iconic images they use, the way the tabs at the top scroll easily, and contact us page that generates an email. Lastly, I've included some photos of the concept we have been working on. What we are trying to demonstrate is how our company offers a range of services that are essentially linked together. We provide individual services that when combined present the full service package. We would like this concept to be integrated into the over concept of our website. Please feel free to ask for clarification of any of the above points or contact us if you have any additional questions. We appreciate all of your hard work and are very excited to see the updated designs. Best, Miriam Dowbrook Plenvaro Senior Program Manager miriam.dowbrook@plenvaro-mail.com

Industry/Entity Type

Government

Font styles to use
Serif
Sans Serif

Requirements
Must have
• Must work on/adapt to various/mobile devices (responsive)
Must be simple and straightforward
Colors should be in line/matching with logo
2 language versions: English and Arabic (no Thai)
Services should be the first group/row of items after/below the main image
Note: the website will be hosted by hostpeak
Nice to have
• Submit feedback form
What's New section
The banner at the bottom of the site should not be too large; we would like a narrow one more
It would be nice if the header/top banner (with Home, About, etc. tabs) could stay in place as you scroll down (like Vortrane and Chatterly)
We will likely only use one image with a Company slogan on the Home page rather than a carousel of images to rotate through
Should not have
• This is the existing website: http://www.plenvaro-example.org
We do not like the animation, the way the banner icons/titles bounce
Not simple enough, we don't like the functionality or how pages load so slowly
We do not like the logo centered - it should be at the left
The banner and its tabs should not be towards the right, we would like them to be centered, to go all the way across and to be below the logo

```html
<!DOCTYPE html>
<html lang="en">
<head>
<meta charset="utf-8">
<title>Plenvaro — Home</title>
<link href="https://fonts.googleapis.com/css2?family=Roboto:wght@300;400;500;700&display=swap" rel="stylesheet">
<style>
:root{
  --red:#e0262c;
  --band:#c1373c;
  --ink:#3b3b3b;
  --muted:#8a8a8a;
  --rule:#dcdcdc;
  --card:#f4f4f4;
  --footer:#3a3a3a;
  --footer-deep:#2b2b2b;
  --footer-text:#d6d6d6;
}
*{margin:0;padding:0;box-sizing:border-box}
html,body{width:960px;height:1200px;overflow:hidden;background:#fff}
body{position:relative;font-family:'Roboto',sans-serif;color:var(--ink)}
.abs{position:absolute}

/* header */
.brand{left:175px;top:30px;display:flex;align-items:center;gap:8px}
.brand-mark{width:14px;height:14px;background:var(--red)}
.brand-name{font-size:19px;font-weight:700;letter-spacing:3px;color:var(--red)}
.nav{left:348px;top:38px;display:flex;align-items:center;font-size:9px;letter-spacing:.3px;color:#555}
.nav a{color:inherit;text-decoration:none;padding:3px 9px;border-left:1px solid #ddd;line-height:10px}
.nav a.active{background:var(--red);color:#fff;border:0;padding:4px 6px;margin-right:9px}
.nav a.active + a{border-left:0}
.search{left:770px;top:38px;width:15px;height:15px;background:var(--red);border-radius:2px}

/* hero */
.hero{left:175px;top:96px;width:611px;height:246px;
  background:radial-gradient(ellipse at 35% 30%,#a81e22 0%,#5e1a1a 35%,transparent 60%),
  radial-gradient(ellipse at 70% 75%,#6b6a1a 0%,transparent 40%),
  linear-gradient(180deg,#2a2626,#1a1818)}
.hero-title{left:175px;top:174px;width:611px;text-align:center;color:#fff;font-size:24px;font-weight:500}
.hero-text{left:230px;top:220px;width:500px;text-align:center;color:#fff;font-size:12px;line-height:19px;font-weight:300}
.services{left:175px;top:342px;width:611px;height:66px;background:var(--band);display:flex}
.service{flex:1;display:flex;flex-direction:column;align-items:center;justify-content:center;gap:6px;color:#fff;font-size:10px}
.service svg{width:20px;height:20px}
.pointer{left:716px;top:328px;width:0;height:0;border-left:9px solid transparent;border-right:9px solid transparent;border-bottom:14px solid var(--band)}

/* section heads */
.sec-head{display:flex;justify-content:space-between;align-items:baseline;border-bottom:1px solid var(--rule);padding-bottom:5px}
.sec-head h2{font-size:12px;font-weight:500;color:#444}
.sec-head a{font-size:8px;color:var(--muted);text-decoration:none}

/* news */
.news-head{left:175px;top:451px;width:611px}
.news{left:176px;top:491px;display:flex;gap:13px}
.card{width:142px;height:207px;background:var(--card)}
.card-photo{height:79px;background:linear-gradient(135deg,#d9d9d9,#8f8f8f)}
.card-photo.c2{background:linear-gradient(135deg,#c9d3dc,#6f8aa5)}
.card-photo.c3{background:linear-gradient(135deg,#d8cfc6,#8c8a8f)}
.card-photo.c4{background:linear-gradient(135deg,#6a5a55,#2c2a30)}
.card h3{font-size:11.5px;font-weight:500;color:#444;margin:10px 0 0 8px}
.card p{font-size:8.3px;line-height:11.6px;color:var(--muted);margin:9px 8px 0 8px}
.card a{display:block;font-size:8.3px;color:var(--red);text-decoration:none;margin:11px 0 0 8px}

/* events */
.events-head{left:175px;top:735px;width:299px}
.event{left:175px;width:299px;display:flex;gap:13px}
.date{width:39px;height:45px;background:#f1f1f1;text-align:center;padding-top:3px;color:#888;font-size:8px;line-height:10px}
.date b{display:block;font-size:12px;font-weight:500;color:#444;line-height:16px}
.event h3{font-size:11.5px;font-weight:500;color:#444;margin-top:-1px}
.event p{font-size:8.3px;line-height:13.5px;color:#666;margin-top:7px}

/* testimonial */
.clients-head{left:486px;top:735px;width:300px}
.arrows{left:760px;top:739px;display:flex;gap:1px}
.arrows span{width:12px;height:11px;background:#cfcfcf;border-radius:3px}
.quote{left:486px;top:774px;width:300px;height:104px;background:#f1f1f1;padding:6px 8px;font-size:8.3px;line-height:13px;color:#666}
.quote-tip{left:526px;top:878px;width:0;height:0;border-left:8px solid transparent;border-right:8px solid transparent;border-top:9px solid #f1f1f1}
.avatar{left:512px;top:901px;width:47px;height:47px;background:linear-gradient(160deg,#cfcac4,#5b5550)}
.author{left:572px;top:919px;font-size:8.3px;color:#555}
.author b{font-weight:500;color:#333}

/* footer */
.footer{left:0;top:986px;width:960px;height:188px;background:var(--footer)}
.foot-col{top:1023px;color:var(--footer-text);font-size:8.3px;line-height:13px}
.foot-col h4{font-size:12px;font-weight:500;color:#cfcfcf;margin-bottom:14px}
.posts div{width:195px;padding-bottom:10px;margin-bottom:10px;border-bottom:1px solid #6a6a6a}
.posts div:last-child{border:0}
.foot-col a{color:inherit}
.socials{display:flex;gap:6px;margin-top:16px}
.socials span{width:16px;height:16px;border-radius:50%;background:#cfcfcf}
.bottom{left:0;top:1174px;width:960px;height:26px;background:var(--footer-deep);color:#d0d0d0;font-size:8.5px;text-align:center;line-height:26px}
</style>
</head>
<body>

<header>
  <div class="abs brand"><span class="brand-mark"></span><span class="brand-name">PLENVARO</span></div>
  <nav class="abs nav">
    <a class="active" href="#">HOME</a><a href="#">BUSINESS UNIT</a><a href="#">SERVICES</a><a href="#">ABOUT US</a><a href="#">LOCATIONS</a><a href="#">CONTACT US</a>
  </nav>
  <div class="abs search">
    <svg viewBox="0 0 15 15" width="15" height="15"><circle cx="6.5" cy="6.5" r="3" fill="none" stroke="#fff" stroke-width="1.5"/><line x1="8.7" y1="8.7" x2="11.5" y2="11.5" stroke="#fff" stroke-width="1.6"/></svg>
  </div>
</header>

<section>
  <div class="abs hero" role="img" aria-label="Blurred close-up of red network cables plugged into a server switch"></div>
  <h1 class="abs hero-title">MAINTENANCE</h1>
  <p class="abs hero-text">Lorem ipsum dolor sit amet, consectetur adipisicing elit,sed do eiusmodtempor incididunt ut labore et dolore magna aliqua.</p>
  <div class="abs pointer"></div>
  <div class="abs services">
    <div class="service">
      <svg viewBox="0 0 20 20"><circle cx="10" cy="6" r="4.5" fill="#fff"/><path d="M2 19c0-5 3.5-7 8-7s8 2 8 7z" fill="#fff"/></svg>Consulting</div>
    <div class="service">
      <svg viewBox="0 0 20 20"><circle cx="10" cy="10" r="6.5" fill="none" stroke="#fff" stroke-width="3.5" stroke-dasharray="3 2.1"/><circle cx="10" cy="10" r="5" fill="none" stroke="#fff" stroke-width="2"/></svg>Engineering</div>
    <div class="service">
      <svg viewBox="0 0 20 20"><line x1="3" y1="17" x2="15" y2="5" stroke="#fff" stroke-width="2.5"/><line x1="5" y1="4" x2="17" y2="16" stroke="#fff" stroke-width="2.5"/><rect x="12" y="2" width="6" height="4" fill="#fff" transform="rotate(45 15 4)"/></svg>Construction</div>
    <div class="service">
      <svg viewBox="0 0 20 20"><circle cx="10" cy="10" r="7" fill="none" stroke="#fff" stroke-width="2" stroke-dasharray="9 2"/><circle cx="10" cy="3" r="2" fill="#fff"/><circle cx="4" cy="14" r="2" fill="#fff"/><circle cx="16" cy="14" r="2" fill="#fff"/></svg>Operations</div>
    <div class="service">
      <svg viewBox="0 0 20 20"><path d="M4 1h12l2 4H2z" fill="#fff"/><rect x="2" y="6" width="16" height="4" fill="#fff"/><rect x="2" y="11" width="16" height="4" fill="#fff"/><rect x="2" y="16" width="16" height="3" fill="#fff"/></svg>Maintenance</div>
  </div>
</section>

<section>
  <div class="abs sec-head news-head"><h2>Latest News</h2><a href="#">View all</a></div>
  <div class="abs news">
    <article class="card"><div class="card-photo" role="img" aria-label="Portrait of a businessman in a suit"></div><h3>Lorem Ipsum</h3><p>Lorem ipsum dolor sit amet, consectetur adipisicing elit, sed do eiusmod tempor incidi-dunt ut labore et dolore magna aliqua.</p><a href="#">Read more</a></article>
    <article class="card"><div class="card-photo c2" role="img" aria-label="Presenter speaking to a seated audience"></div><h3>Lorem Ipsum</h3><p>Lorem ipsum dolor sit amet, consectetur adipisicing elit, sed do eiusmod tempor incidi-dunt ut labore et dolore magna aliqua.</p><a href="#">Read more</a></article>
    <article class="card"><div class="card-photo c3" role="img" aria-label="Colleagues in a meeting at a table"></div><h3>Lorem Ipsum</h3><p>Lorem ipsum dolor sit amet, consectetur adipisicing elit, sed do eiusmod tempor incidi-dunt ut labore et dolore magna aliqua.</p><a href="#">Read more</a></article>
    <article class="card"><div class="card-photo c4" role="img" aria-label="Business audience applauding"></div><h3>Lorem Ipsum</h3><p>Lorem ipsum dolor sit amet, consectetur adipisicing elit, sed do eiusmod tempor incidi-dunt ut labore et dolore magna aliqua.</p><a href="#">Read more</a></article>
  </div>
</section>

<section>
  <div class="abs sec-head events-head"><h2>Event Updates</h2><a href="#">View all</a></div>
  <div class="abs event" style="top:774px"><div class="date"><b>17</b>MAY<br>2014</div><div><h3>Lorem Ipsum</h3><p>Lorem ipsum dolor sit amet, consectetur adipiscing elit. Nulla vehicula feugiat blandit. Nulla facilisi. Nulla tellus nisi...</p></div></div>
  <div class="abs event" style="top:838px"><div class="date"><b>04</b>MAY<br>2014</div><div><h3>Lorem Ipsum</h3><p>Lorem ipsum dolor sit amet, consectetur adipiscing elit. Nulla vehicula feugiat blandit. Nulla facilisi. Nulla tellus nisi...</p></div></div>
  <div class="abs event" style="top:902px"><div class="date"><b>23</b>APRIL<br>2014</div><div><h3>Lorem Ipsum</h3><p>Lorem ipsum dolor sit amet, consectetur adipiscing elit. Nulla vehicula feugiat blandit. Nulla facilisi. Nulla tellus nisi...</p></div></div>
</section>

<section>
  <div class="abs sec-head clients-head"><h2>What Clients Say</h2></div>
  <div class="abs arrows"><span></span><span></span></div>
  <blockquote class="abs quote">Fusce ele mentum, nulla vel pellentesque consequat, ante nulla hen-drerit arcu, ac tincidunt mauris lacus sed leo. vamus suscipit molestie vestibulum.Fusce elementum, nulla vel pellentesque consequat, ante nulla hendrerit arcu, ac tincidunt mauris lacus sed leo. vamus suscipit molestie vestibulum.Fusce elementum, nulla vel pellentesque conse-quat, ante nulla hendrerit arcu, ac tincidunt mauris lacus sed leo. vamus suscipit molestie vestibulum.</blockquote>
  <div class="abs quote-tip"></div>
  <div class="abs avatar" role="img" aria-label="Portrait of the client"></div>
  <div class="abs author"><b>John Doe</b> - CEO Plenvaro</div>
</section>

<footer>
  <div class="abs footer"></div>
  <div class="abs foot-col" style="left:175px;width:190px">
    <h4>Plenvaro</h4>
    <p>Plenvaro is a joint venture between tarnwell construction, korvex worldwide and aldane engineer-ing &amp; management company founded in bang-kok, thailand in 2003 and meridel electrical con-struction company founded in san francisco, california in 2001.</p>
  </div>
  <div class="abs foot-col posts" style="left:382px">
    <h4>Latest Posts</h4>
    <div>Lorem ipsum dolor sit amet consectetur.</div>
    <div>Lorem ipsum dolor sit amet consectetur.</div>
    <div>Lorem ipsum dolor sit amet consectetur.</div>
  </div>
  <div class="abs foot-col" style="left:590px;width:200px">
    <h4>Get in touch</h4>
    <p>Contact with us via our <a href="#">contact form</a> or follow us on our social networks.</p>
    <div class="socials"><span></span><span></span><span></span></div>
  </div>
  <div class="abs bottom">Plenvaro © 2014 - All Rights Reserved</div>
</footer>

</body>
</html>
```